Re-branding for Structural Engineering firm

We need new business cards as part of our current re-branding. We have a new logo (attached), so the card design should incorporate this color scheme. We are a structural engineering firm providing structural building design and seismic consulting services. The final design should communicate professionalism and stability, with a modern look and feel.

```html
<!DOCTYPE html>
<html lang="en">
<head>
<meta charset="utf-8">
<title>Halvorsen Structural Engineering – Business Card</title>
<link href="https://fonts.googleapis.com/css2?family=Lato:wght@400;700&family=Open+Sans:wght@400;600;700&display=swap" rel="stylesheet">
<style>
  :root {
    --brand-blue: #1b75bc;
    --brand-grey: #8a8c8f;
    --band-grey: #7d7f82;
    --card-white: #ffffff;
    --stage: #eceef0;
    --text-white: #ffffff;
  }
  * { margin: 0; padding: 0; box-sizing: border-box; }
  html, body {
    width: 1200px; height: 900px; overflow: hidden;
    background: var(--stage);
  }
  .canvas { position: relative; width: 1200px; height: 900px; }

  .card {
    position: absolute;
    box-shadow: 0 6px 18px rgba(0,0,0,0.18);
    overflow: hidden;
  }

  /* Front */
  .card-front {
    left: 78px; top: 34px; width: 588px; height: 363px;
    background: var(--card-white);
  }
  .front-bands { position: absolute; inset: 0; }
  .brand-lockup {
    position: absolute; left: 111px; top: 58px;
    display: flex; align-items: center; gap: 14px;
  }
  .brand-square {
    width: 72px; height: 74px; background: var(--brand-blue);
  }
  .brand-name {
    font-family: "Lato", sans-serif; font-weight: 700;
    color: var(--brand-blue); font-size: 36px; line-height: 38px;
    letter-spacing: 0.5px; text-transform: uppercase;
  }
  .contact-list {
    position: absolute; left: 27px; top: 252px;
    list-style: none;
    font-family: "Open Sans", sans-serif; font-size: 15px;
    color: var(--text-white); line-height: 21px;
  }
  .contact-list li { display: flex; align-items: center; gap: 8px; }
  .contact-list svg { width: 13px; height: 13px; flex: none; }
  .person {
    position: absolute; right: 36px; top: 240px; text-align: right;
    font-family: "Open Sans", sans-serif; color: var(--text-white);
  }
  .person-name { font-weight: 700; font-size: 17px; line-height: 22px; }
  .person-title { font-size: 15px; line-height: 20px; }
  .person-address { margin-top: 16px; font-size: 15px; line-height: 21px; }

  /* Back */
  .card-back {
    left: 388px; top: 505px; width: 567px; height: 352px;
    background: var(--brand-blue);
    display: flex; align-items: center; justify-content: center; gap: 18px;
  }
  .back-square {
    width: 60px; height: 60px; background: #e6e7e8;
  }
  .back-name {
    font-family: "Lato", sans-serif; font-weight: 700;
    color: var(--text-white); font-size: 40px; letter-spacing: 2px;
    text-transform: uppercase;
  }
</style>
</head>
<body>
<main class="canvas">

  <section class="card card-front" aria-label="Business card front">
    <svg class="front-bands" width="588" height="363" viewBox="0 0 588 363" aria-hidden="true">
      <polygon points="0,190 400,190 380,214 0,214" fill="var(--band-grey)"/>
      <polygon points="0,217 382,217 412,181 588,181 588,363 0,363" fill="var(--brand-blue)"/>
    </svg>

    <div class="brand-lockup">
      <div class="brand-square"></div>
      <div class="brand-name">Halvorsen<br>Engineering</div>
    </div>

    <ul class="contact-list">
      <li>
        <svg viewBox="0 0 16 16"><path d="M2 5c0-2 2-3 6-3s6 1 6 3v1h-3V5H5v1H2zM4 7h8l2 7H2z" fill="#fff"/></svg>
        555.210.4387
      </li>
      <li>
        <svg viewBox="0 0 16 16"><rect x="4" y="1" width="8" height="14" rx="1.5" fill="none" stroke="#fff" stroke-width="1.6"/><circle cx="8" cy="12.5" r="0.9" fill="#fff"/></svg>
        555.384.9021
      </li>
      <li>
        <svg viewBox="0 0 16 16"><rect x="1" y="3" width="14" height="10" fill="#fff"/><path d="M1 3l7 6 7-6" fill="none" stroke="var(--brand-blue)" stroke-width="1.3"/></svg>
        dale@halvorsense.com
      </li>
      <li>
        <svg viewBox="0 0 16 16"><circle cx="8" cy="8" r="7" fill="#fff"/><path d="M4 5c2 0 2 2 4 2s1 3 3 3M6 13c0-2 2-2 2-4" fill="none" stroke="var(--brand-blue)" stroke-width="1.2"/></svg>
        www.halvorsense.com
      </li>
    </ul>

    <div class="person">
      <p class="person-name">DALE MORVEN, S.E.</p>
      <p class="person-title">Principal</p>
      <p class="person-address">4150 Harbor Ridge Ave.,<br>Ste 210 Bayview, CA 90210</p>
    </div>
  </section>

  <section class="card card-back" aria-label="Business card back">
    <div class="back-square"></div>
    <div class="back-name">Halvorsen</div>
  </section>

</main>
</body>
</html>
```